www.brevatin.com Sales/Order Page ReDesign

We need a new and amazing design for our sales/order page to attract more costumers and new houses for our portal.

Here is the existing page with the current design: https://www.brevatin.com/sales

We are proud owners of www.sommarhytta.no and www.brevatin.com and we want more holiday home owners to join our page so that we can rent out their holiday homes and increase the number of houses on our portal.

To get more homeowners we need a sales page that can sell our products the best way possible. Therefore we want you too blow us away with a fresh, modern, easy understandable and stylish new sales/order page.

The only restrictions we give when it comes to design is that it needs to fit the existing design of our portals, the top and footer are set. Beside that we are open for everything as long as it at once give the customers impression that this is a good, professional page were they just have to put out their houses.

When it comes to content I have added two documents who include the content to put in here and some guidelines on how to organize the page. Please be creative and add necessary graphics, symbols, background pictures and what ever necessary to make this page look professional and appealing to new costumers.

Looking forward to what suggestions we are given.

We just want to inform that we have updated our brief with a much more concrete description of what content to add on the sale page, and who to structure the content on the page. Hope this helps to make suggestions easier. Looking forward to receive some good contributions.

We would just like to make sure that everyone have understood that we are not asking for a new design suggestion to our portal in general. We are only asking for a redesign of our sales/order page you find here www.brevatin.com/sales. We have to day received some designs for our front page and the design it self was good, but that's not what we are asking for this time and don't want you to use time of something we don't need at the moment. We are looking forward too se some good suggestions.

Reason: Hello. Thanks for all the great contributions we have been given so fare. We haven't been able to respond to all design and are therefore extending the deadline so that we are able to respond to the designs we have been giver and to gov time to make final changes.

Reason: We are extending the deadline to give designers time to give new suggestion based on our latest feedback today.

Reason: Extended so we can receive last design changes.

Target Market(s)

This is a presentation page where we present our product agains new home owner who we what to choose listing there property on or site.

Industry/Entity Type

Sales

Requirements
Must have
• A modern design who calms the costumer down and help them in deciding to chose us, and for them to choose us they need to trust and believe in us. Therefore your main task is to create a page that effectively informs about our product, gets the visitors attentions and make them trust us.
Nice to have
• Examples of good competitors and good order pages we like:

http://www.cabinquest.example/info/lyp?icid=IL___O_Text___top_nav_link
https://www.nestlodge.example/rooms/new
https://www.pearvix.example/phone/compare/
http://www.guestnook.example/host
Should not have
• - Bad design :-). With bad design we mean design that looks like it's made in 2 seconds by a little child.

```html
<!DOCTYPE html>
<html lang="en">
<head>
<meta charset="utf-8">
<title>Brevatin – List your property</title>
<link rel="stylesheet" href="https://fonts.googleapis.com/css2?family=Open+Sans:wght@400;600;700&family=Ubuntu:wght@400;500&family=Questrial&display=swap">
<style>
:root{
  --blue:#1a93dc;
  --blue-dark:#0b78c2;
  --bar-top:#2c9be2;
  --bar-bottom:#0a74c0;
  --ink:#333333;
  --ink-soft:#444444;
  --page:#f5f5f5;
  --rule:#dcdcdc;
  --panel:#e9e9e9;
  --green:#9ccc2c;
  --green-dark:#76a51b;
  --chevron:#2f2f2f;
  --icon-dark:#3a3a3a;
  --red:#d62d2d;
  --navy:#1f3d8a;
}
*{box-sizing:border-box;margin:0;padding:0}
html,body{width:822px;height:1200px;overflow:hidden;background:var(--page)}
body{font-family:"Open Sans",Arial,sans-serif;color:var(--ink);position:relative}
.page{position:relative;width:822px;height:1200px}
.top-bar{position:absolute;left:0;top:0;width:822px;height:37px;background:linear-gradient(var(--bar-top),var(--bar-bottom));box-shadow:0 2px 3px rgba(0,0,0,.2)}
.brand-tab{position:absolute;left:103px;top:0;width:221px;height:112px;background:linear-gradient(#ffffff,#ececec);box-shadow:0 2px 6px rgba(0,0,0,.25)}
.brand-tab svg.chevron{position:absolute;left:0;bottom:0}
.brand-name{position:absolute;left:22px;top:24px;display:flex;align-items:center;gap:10px;font-family:"Ubuntu",sans-serif;font-weight:500;font-size:30px;color:var(--blue)}
.brand-mark{width:26px;height:26px;background:var(--blue)}
.flags{position:absolute;left:465px;top:9px;display:flex;gap:6px}
.sign-in{position:absolute;left:523px;top:5px;width:105px;height:27px;border-radius:3px;background:linear-gradient(#b6dc4a,var(--green));border:1px solid var(--green-dark);font-size:10px;font-weight:600;color:#3b5a08;display:flex;align-items:center;padding-left:14px;gap:10px}
.sign-in .caret{position:absolute;right:12px;top:11px;border:4px solid transparent;border-top-color:#3b5a08}
.list-link{position:absolute;left:635px;top:10px;font-size:11px;font-weight:700;color:#fff}
.multi-link{position:absolute;left:588px;top:47px;display:flex;align-items:center;gap:8px;font-size:10px;font-weight:600;color:var(--blue)}
.hero-title{position:absolute;left:0;top:126px;width:822px;text-align:center;font-family:"Ubuntu",sans-serif;font-weight:500;font-size:35px;color:var(--blue);letter-spacing:.5px}
.hero-sub{position:absolute;left:0;top:168px;width:822px;text-align:center;font-family:"Ubuntu",sans-serif;font-size:16px;color:var(--ink-soft);letter-spacing:.4px}
.rule-top{position:absolute;left:0;top:197px;width:822px;height:1px;background:var(--rule)}
.hero-photo{position:absolute;left:0;top:201px;width:822px;height:186px;background:linear-gradient(180deg,#b9a98a 0%,#f0b95a 30%,#e9a244 45%,#7c7163 58%,#3b3a38 78%,#1d1d1d 100%)}
.hero-line{position:absolute;font-family:"Questrial",sans-serif;color:#1b1b1b;font-size:23px}
.hero-line.one{left:124px;top:46px}
.hero-line.two{left:211px;top:72px;font-size:21px}
.section-title{position:absolute;left:0;top:406px;width:822px;text-align:center;font-size:15px;font-weight:700;color:var(--ink);letter-spacing:.3px}
.rule-section{position:absolute;left:88px;top:437px;width:646px;height:1px;background:var(--rule)}
.feature{position:absolute;width:210px;text-align:center}
.feature svg{display:block;margin:0 auto;height:46px}
.feature h3{margin-top:12px;font-size:12.5px;font-weight:600;color:var(--blue)}
.feature p{margin-top:9px;font-size:8.3px;line-height:11.6px;color:var(--ink)}
.c1{left:83px}.c2{left:315px}.c3{left:523px}
.r1{top:456px}.r2{top:604px}.r3{top:763px}.r4{top:918px}
.prices-line{position:absolute;left:0;top:1093px;width:822px;text-align:center;font-size:16px;color:var(--ink)}
.rule-prices{position:absolute;left:88px;top:1130px;width:646px;height:1px;background:var(--rule)}
.discount-panel{position:absolute;left:88px;top:1142px;width:644px;height:58px;background:var(--panel);display:flex;align-items:center;padding-left:74px;gap:14px}
.discount-panel label{font-size:11px;font-weight:600;color:var(--ink)}
.discount-panel .count-input{width:186px;height:27px;background:#fff;border:1px solid #bdbdbd;font-size:8.5px;color:#888;display:flex;align-items:center;padding-left:10px}
</style>
</head>
<body>
<div class="page">
  <header>
    <div class="top-bar"></div>
    <div class="brand-tab">
      <div class="brand-name"><span class="brand-mark"></span>Brevatin</div>
      <svg class="chevron" width="221" height="46" viewBox="0 0 221 46"><path d="M0 26 L110 6 L221 26 L221 46 L110 22 L0 46Z" fill="var(--chevron)"/></svg>
    </div>
    <div class="flags">
      <svg width="20" height="14" viewBox="0 0 20 14" aria-label="Norwegian"><rect width="20" height="14" fill="var(--red)"/><rect x="5" width="4" height="14" fill="#fff"/><rect y="5" width="20" height="4" fill="#fff"/><rect x="6" width="2" height="14" fill="var(--navy)"/><rect y="6" width="20" height="2" fill="var(--navy)"/></svg>
      <svg width="24" height="14" viewBox="0 0 24 14" aria-label="English"><rect width="24" height="14" fill="var(--navy)"/><path d="M0 0 L24 14 M24 0 L0 14" stroke="#fff" stroke-width="3"/><path d="M0 0 L24 14 M24 0 L0 14" stroke="var(--red)" stroke-width="1"/><rect x="10" width="4" height="14" fill="#fff"/><rect y="5" width="24" height="4" fill="#fff"/><rect x="11" width="2" height="14" fill="var(--red)"/><rect y="6" width="24" height="2" fill="var(--red)"/></svg>
    </div>
    <div class="sign-in"><svg width="7" height="9" viewBox="0 0 7 9"><rect y="4" width="7" height="5" fill="#3b5a08"/><path d="M1.5 4 V2.5 a2 2 0 0 1 4 0 V4" stroke="#3b5a08" fill="none" stroke-width="1.2"/></svg>Sign in<span class="caret"></span></div>
    <div class="list-link">List your property</div>
    <div class="multi-link"><svg width="12" height="11" viewBox="0 0 12 11"><path d="M6 0 L12 5 H10 V11 H7 V7 H5 V11 H2 V5 H0Z" fill="var(--blue)"/></svg>Advertising 5+ properties?</div>
  </header>

  <main>
    <h1 class="hero-title">LIST YOUR PROPERTY TODAY!</h1>
    <p class="hero-sub">BREVATIN HELPS YOU MAKE MONEY ON YOUR PROPERTY, STARTING NOW...</p>
    <div class="rule-top"></div>
    <div class="hero-photo" role="img" aria-label="Sunset over a rocky beach with a holiday house on the right">
      <span class="hero-line one">On Brevatin you can rent out:</span>
      <span class="hero-line two">Your Slogan</span>
    </div>

    <h2 class="section-title">ALL OUR ANNOUNCEMENTS HAVE THE FOLLOWING SERVICES INCLUDED:</h2>
    <div class="rule-section"></div>

    <section class="feature c1 r1">
      <svg viewBox="0 0 46 46"><circle cx="23" cy="23" r="20" fill="none" stroke="var(--icon-dark)" stroke-width="3.5"/><circle cx="23" cy="18" r="7" fill="var(--blue)"/><path d="M11 36 a12 11 0 0 1 24 0Z" fill="var(--blue)"/></svg>
      <h3>Help from professionals</h3>
      <p>Let professionals who know the travel industries handle all yours booking requests. Great result with less work, our professional team will answer all you inquiries, while you.......</p>
    </section>
    <section class="feature c2 r1">
      <svg viewBox="0 0 46 46"><rect x="4" y="10" width="38" height="26" fill="var(--red)"/><rect x="14" y="10" width="8" height="26" fill="#fff"/><rect x="4" y="19" width="38" height="8" fill="#fff"/><rect x="16" y="10" width="4" height="26" fill="var(--navy)"/><rect x="4" y="21" width="38" height="4" fill="var(--navy)"/></svg>
      <h3>Access Scandinavians</h3>
      <p>Our roots are from Norway, and we have expertise with the Scandinavian market and can help you get tenants from these very travel friendly demographics.</p>
    </section>
    <section class="feature c3 r1">
      <svg viewBox="0 0 46 46"><path d="M8 18 H16 L34 8 V38 L16 28 H8Z" fill="var(--blue)"/><rect x="11" y="28" width="6" height="10" fill="var(--blue)"/><rect x="36" y="19" width="5" height="8" fill="var(--blue)"/></svg>
      <h3>Broad exposure</h3>
      <p>We have been in the market for several years and are promoting your property through the necessary and right channels.</p>
    </section>

    <section class="feature c1 r2">
      <svg viewBox="0 0 46 46"><path d="M23 4 L40 10 V22 C40 33 32 40 23 43 C14 40 6 33 6 22 V10Z" fill="var(--icon-dark)"/><path d="M23 9 L35 13.5 V22 C35 30 29.5 35 23 38Z" fill="var(--blue)"/></svg>
      <h3>Trust &amp; Safety</h3>
      <p>You are still in control of your property. We have the tools to help you accept a booking only if you're 100% comfortable.</p>
    </section>
    <section class="feature c2 r2">
      <svg viewBox="0 0 46 46"><circle cx="23" cy="20" r="15" fill="none" stroke="var(--blue)" stroke-width="3" stroke-dasharray="4 3"/><circle cx="23" cy="20" r="10" fill="#fff" stroke="var(--icon-dark)" stroke-width="2"/><text x="23" y="25" text-anchor="middle" font-family="Open Sans,sans-serif" font-weight="700" font-size="14" fill="var(--icon-dark)">$</text><rect x="18" y="35" width="10" height="3" fill="var(--icon-dark)"/><rect x="19" y="40" width="8" height="3" fill="var(--icon-dark)"/></svg>
      <h3>No Traveler fees</h3>
      <p>Unlike many other vacation rental booking sites, travelers can book vacation rentals without paying any fees to us, maybe one of the reason we have so many returning costumers.</p>
    </section>
    <section class="feature c3 r2">
      <svg viewBox="0 0 56 46"><rect x="6" y="5" width="44" height="30" fill="var(--icon-dark)"/><rect x="4" y="10" width="48" height="30" fill="#4f8e4f"/><rect x="8" y="14" width="40" height="22" fill="none" stroke="#fff" stroke-width="1.5"/><text x="28" y="32" text-anchor="middle" font-family="Open Sans,sans-serif" font-weight="700" font-size="17" fill="#fff">$</text></svg>
      <h3>Payments by Brevatin</h3>
      <p>Guests are always carful when it comes to payment. Everybody can feel safe through secure payment with Brevatin. We are responsible for you getting paid.</p>
    </section>

    <section class="feature c1 r3">
      <svg viewBox="0 0 54 46"><rect x="3" y="8" width="46" height="20" rx="3" fill="#fff" stroke="var(--icon-dark)" stroke-width="2"/><text x="26" y="22" text-anchor="middle" font-family="Open Sans,sans-serif" font-weight="700" font-size="10" fill="var(--icon-dark)">www://</text><path d="M30 24 L45 32 L39 34 L44 42 L41 43.5 L36.5 35.5 L32 40Z" fill="var(--icon-dark)"/></svg>
      <h3>Online Booking</h3>
      <p>We simplify the booking process by allowing tenants to send online reservations request, which gives you a 24-hour period to accept or decline their reservation.</p>
    </section>
    <section class="feature c2 r3">
      <svg viewBox="0 0 46 46"><circle cx="22" cy="22" r="14" fill="none" stroke="var(--icon-dark)" stroke-width="6" stroke-dasharray="5 4"/><circle cx="22" cy="22" r="11" fill="var(--icon-dark)"/><circle cx="22" cy="22" r="5" fill="var(--page)"/><path d="M20 18 L38 38" stroke="var(--blue)" stroke-width="5" stroke-linecap="round"/></svg>
      <h3>Easy-to-Use Tools</h3>
      <p>Get access too a very well developed reservation and management tool that helps you keep track of bookings.</p>
    </section>
    <section class="feature c3 r3">
      <svg viewBox="0 0 46 46"><circle cx="23" cy="23" r="20" fill="var(--blue-dark)"/><text x="23" y="32" text-anchor="middle" font-family="Open Sans,sans-serif" font-weight="700" font-size="26" fill="#fff">?</text></svg>
      <h3>Unlimited inquiries</h3>
      <p>When you are renting out your property you need inquiries, therefore we have no fees on inquiries for your property.</p>
    </section>

    <section class="feature c1 r4">
      <svg viewBox="0 0 46 46"><circle cx="23" cy="23" r="20" fill="none" stroke="var(--blue)" stroke-width="3"/><rect x="12" y="17" width="22" height="15" rx="2" fill="var(--blue)"/><rect x="18" y="14" width="8" height="4" fill="var(--blue)"/><circle cx="23" cy="24.5" r="4.5" fill="#fff"/><circle cx="23" cy="24.5" r="2.5" fill="var(--blue)"/></svg>
      <h3>Unlimited photos</h3>
      <p>A picture says more then 1000 words, therefore we inspire you too upload as many pictures as possible.</p>
    </section>
    <section class="feature c2 r4">
      <svg viewBox="0 0 50 46"><rect x="4" y="7" width="32" height="30" rx="2" fill="var(--icon-dark)"/><rect x="10" y="3" width="3" height="7" fill="var(--icon-dark)"/><rect x="27" y="3" width="3" height="7" fill="var(--icon-dark)"/><g fill="#fff"><rect x="8" y="16" width="5" height="4"/><rect x="16" y="16" width="5" height="4"/><rect x="24" y="16" width="5" height="4"/><rect x="8" y="23" width="5" height="4"/><rect x="16" y="23" width="5" height="4"/><rect x="8" y="30" width="5" height="4"/></g><circle cx="36" cy="32" r="10" fill="#fff" stroke="var(--icon-dark)" stroke-width="2.5"/><path d="M36 26 V32 H40" stroke="var(--icon-dark)" stroke-width="2" fill="none"/></svg>
      <h3>Online calendar</h3>
      <p>Tenants like to know when your property is available straight away, and we let them know that. At the same time you can easily manage your availability.</p>
    </section>
    <section class="feature c3 r4">
      <svg viewBox="0 0 46 46"><path d="M5 12 L16 8 L30 12 L41 8 V38 L30 42 L16 38 L5 42Z" fill="var(--icon-dark)"/><path d="M23 9 a7 7 0 0 1 7 7 c0 5 -7 13 -7 13 s-7 -8 -7 -13 a7 7 0 0 1 7 -7Z" fill="#fff"/><circle cx="23" cy="16" r="2.6" fill="var(--icon-dark)"/></svg>
      <h3>Map and location</h3>
      <p>Tenants are always wondering where your property is located. Show them through our map and let them know where nearby attractions are.</p>
    </section>

    <p class="prices-line">Getting impressed now, wait to you see our low prices...</p>
    <div class="rule-prices"></div>
    <div class="discount-panel">
      <label>Get discounts if you have more than one property</label>
      <div class="count-input">Type in the number of properties</div>
    </div>
  </main>
</div>
</body>
</html>
```